International Wholesale Food Company Needs Packaging Design for new products

We have a logo for our new business. It is attached. Now we need a packaging design for some new products that we will be selling. These items will be packaged in clear plastic bags. We are an international wholesale foods company selling foods imported from West Africa. We are just in the process of launching. We're looking for a design that is fresh and modern.

These items below are what we need packaging design for:

Cassava Leaves-500 g- Clear Plastic Bag
Sweet potato leaves-500 g-Clear Plastic Bag

```html
<!DOCTYPE html>
<html lang="en">
<head>
<meta charset="utf-8">
<title>Baobab Pantry – Leaf Packaging</title>
<link rel="stylesheet" href="https://fonts.googleapis.com/css2?family=Montserrat:wght@600;800;900&family=Oswald:wght@500;600&family=Caveat:wght@600&display=swap">
<style>
  :root {
    --page: #ffffff;
    --film: #f3f4f5;
    --film-edge: #d9dcde;
    --seal-line: #c9cdd0;
    --leaf-dark: #2f5e22;
    --leaf-mid: #4f8a33;
    --leaf-light: #6fa64a;
    --cassava-label: #8bcf3a;
    --cassava-ink: #1d6a2e;
    --potato-label: #e8621f;
    --potato-ink: #f5d31c;
    --badge: #1a1a1a;
    --white: #ffffff;
  }
  html, body {
    margin: 0;
    padding: 0;
    width: 1200px;
    height: 746px;
    overflow: hidden;
    background: var(--page);
  }
  .canvas { display: block; width: 1200px; height: 746px; }
  .bag-film { fill: var(--film); stroke: var(--film-edge); stroke-width: 1.5; }
  .seal-line { stroke: var(--seal-line); stroke-width: 1; }
  .label-cassava { fill: var(--cassava-label); }
  .label-potato { fill: var(--potato-label); }
  .brand-ring { fill: none; stroke: var(--white); stroke-width: 3; }
  .brand-name { font-family: "Montserrat", sans-serif; font-weight: 600; font-size: 12px; fill: var(--white); letter-spacing: 0.2px; }
  .product-name { font-family: "Montserrat", sans-serif; font-weight: 900; }
  .cassava-ink { fill: var(--cassava-ink); }
  .potato-ink { fill: var(--potato-ink); }
  .tagline { font-family: "Caveat", cursive; font-weight: 600; font-size: 25px; fill: var(--white); }
  .claim { font-family: "Oswald", sans-serif; font-weight: 500; font-size: 15px; letter-spacing: 0.2px; }
  .badge { fill: var(--badge); }
  .badge-text { font-family: "Caveat", cursive; font-weight: 600; font-size: 21px; fill: var(--white); }
  .weight { font-family: "Oswald", sans-serif; font-weight: 600; font-size: 30px; fill: var(--white); }
  .web { font-family: "Oswald", sans-serif; font-weight: 500; font-size: 12px; fill: var(--white); letter-spacing: 0.3px; }
</style>
</head>
<body>
<svg class="canvas" viewBox="0 0 1200 746" xmlns="http://www.w3.org/2000/svg">
  <defs>
    <radialGradient id="leaves-spinach" cx="50%" cy="50%" r="60%">
      <stop offset="0" stop-color="var(--leaf-mid)"/>
      <stop offset="1" stop-color="var(--leaf-dark)"/>
    </radialGradient>
    <radialGradient id="leaves-rocket" cx="50%" cy="50%" r="60%">
      <stop offset="0" stop-color="var(--leaf-light)"/>
      <stop offset="1" stop-color="var(--leaf-dark)"/>
    </radialGradient>
  </defs>

  <!-- Cassava leaves bag -->
  <g class="bag bag-cassava">
    <rect class="bag-film" x="103" y="130" width="460" height="515" rx="10"/>
    <g class="seal">
      <line class="seal-line" x1="105" y1="136" x2="561" y2="136"/>
      <line class="seal-line" x1="105" y1="142" x2="561" y2="142"/>
      <line class="seal-line" x1="105" y1="148" x2="561" y2="148"/>
      <line class="seal-line" x1="105" y1="627" x2="561" y2="627"/>
      <line class="seal-line" x1="105" y1="633" x2="561" y2="633"/>
      <line class="seal-line" x1="105" y1="639" x2="561" y2="639"/>
    </g>
    <rect x="140" y="175" width="385" height="430" rx="60" fill="url(#leaves-spinach)" role="img" aria-label="Fresh cassava leaves visible through the clear bag"/>
    <circle class="label-cassava" cx="279" cy="377" r="141"/>
    <circle class="brand-ring" cx="281" cy="300" r="30"/>
    <text class="brand-name" x="281" y="345" text-anchor="middle">BAOBAB PANTRY</text>
    <text class="product-name cassava-ink" x="281" y="391" text-anchor="middle" font-size="39">CASSAVA</text>
    <text class="product-name cassava-ink" x="281" y="421" text-anchor="middle" font-size="29">LEAVES</text>
    <text class="tagline" x="281" y="448" text-anchor="middle">Natural, Fresh, Healthy!</text>
    <text class="claim cassava-ink" x="281" y="472" text-anchor="middle">WASHED &amp; READY TO EAT!</text>
    <circle class="badge" cx="231" cy="534" r="43"/>
    <text class="badge-text" x="231" y="527" text-anchor="middle">100%</text>
    <text class="badge-text" x="231" y="548" text-anchor="middle">organic!</text>
    <text class="weight" x="496" y="553" text-anchor="end">500 G</text>
    <text class="web" x="496" y="573" text-anchor="end">BAOBABPANTRY.COM</text>
  </g>

  <!-- Sweet potato leaves bag -->
  <g class="bag bag-potato">
    <rect class="bag-film" x="647" y="130" width="460" height="515" rx="10"/>
    <g class="seal">
      <line class="seal-line" x1="649" y1="136" x2="1105" y2="136"/>
      <line class="seal-line" x1="649" y1="142" x2="1105" y2="142"/>
      <line class="seal-line" x1="649" y1="148" x2="1105" y2="148"/>
      <line class="seal-line" x1="649" y1="627" x2="1105" y2="627"/>
      <line class="seal-line" x1="649" y1="633" x2="1105" y2="633"/>
      <line class="seal-line" x1="649" y1="639" x2="1105" y2="639"/>
    </g>
    <rect x="684" y="175" width="385" height="430" rx="60" fill="url(#leaves-rocket)" role="img" aria-label="Fresh sweet potato leaves visible through the clear bag"/>
    <circle class="label-potato" cx="817" cy="377" r="137"/>
    <circle class="brand-ring" cx="817" cy="298" r="30"/>
    <text class="brand-name" x="817" y="338" text-anchor="middle">BAOBAB PANTRY</text>
    <text class="product-name potato-ink" x="718" y="364" font-size="21">SWEET</text>
    <text class="product-name potato-ink" x="820" y="398" text-anchor="middle" font-size="36">POTATO</text>
    <text class="product-name potato-ink" x="830" y="426" text-anchor="middle" font-size="28">LEAVES</text>
    <text class="tagline" x="817" y="452" text-anchor="middle">Natural, Fresh, Healthy!</text>
    <text class="claim potato-ink" x="814" y="476" text-anchor="middle">WASHED &amp; READY TO EAT!</text>
    <circle class="badge" cx="770" cy="534" r="43"/>
    <text class="badge-text" x="770" y="527" text-anchor="middle">100%</text>
    <text class="badge-text" x="770" y="548" text-anchor="middle">organic!</text>
    <text class="weight" x="1038" y="549" text-anchor="end">500 G</text>
    <text class="web" x="1038" y="569" text-anchor="end">BAOBABPANTRY.COM</text>
  </g>
</svg>
</body>
</html>
```